Contemporary Vehicle wrap design

Looking for a contemporary design vehicle wrap. This is for a kitchen and bath remodeling company. We have a Hallard K-270 Truck, Hallard Meridel Cargo Van and a 12’ enclosed trailer. Attached is our logo

Industry/Entity Type

Construction

Colors

Designer to choose colors to be used in the design.

```html
<!DOCTYPE html>
<html lang="en">
<head>
<meta charset="utf-8">
<title>Norvale Design – Fleet Wrap</title>
<link rel="stylesheet" href="https://fonts.googleapis.com/css2?family=Archivo+Black&family=Montserrat:wght@300;600;800&family=Oswald:wght@500;600&display=swap">
<style>
  :root{
    --ink:#1b1b1b;
    --rocker:#2c2c2c;
    --body:#f3f3f1;
    --olive:#c7bf2c;
    --leaf:#6b8e3a;
    --lime:#96b552;
    --ring:#6f6f6f;
    --paper:#ffffff;
  }
  html,body{margin:0;padding:0;overflow:hidden;}
  body{background:var(--paper);}
  .canvas{position:relative;width:855px;height:1200px;overflow:hidden;background:var(--paper);}
  .wrap-panel{position:absolute;left:30px;width:795px;display:block;}
  .wrap-van{top:30px;height:300px;}
  .wrap-truck{top:380px;height:270px;}
  .wrap-trailer{top:690px;height:490px;}
  .brand-name{font-family:"Oswald",sans-serif;font-weight:600;letter-spacing:1px;}
  .service-line{font-family:"Archivo Black",sans-serif;}
  .phone{font-family:"Montserrat",sans-serif;font-weight:800;}
  .web{font-family:"Montserrat",sans-serif;font-weight:300;}
  .tagline{font-family:"Oswald",sans-serif;font-weight:500;}
  .small-service{font-family:"Montserrat",sans-serif;font-weight:600;}
</style>
</head>
<body>
<main class="canvas">

  <!-- Cargo van wrap -->
  <svg class="wrap-panel wrap-van" viewBox="0 0 795 300" aria-label="Cargo van wrap layout">
    <rect class="body-base" x="0" y="0" width="795" height="280" rx="24" fill="var(--body)"/>
    <path class="black-field" d="M430 0 H771 Q795 0 795 24 V150 H430 Z" fill="var(--ink)"/>
    <rect class="olive-band" x="430" y="150" width="365" height="32" fill="var(--olive)"/>
    <rect class="leaf-band" x="430" y="182" width="365" height="38" fill="var(--leaf)"/>
    <circle class="brand-ring" cx="400" cy="135" r="108" fill="var(--body)" stroke="var(--ring)" stroke-width="14"/>
    <text class="brand-name" x="400" y="150" font-size="44" fill="var(--leaf)" text-anchor="middle">NORVALE</text>
    <path class="rocker" d="M0 220 H795 V256 Q795 280 771 280 H24 Q0 280 0 256 Z" fill="var(--rocker)"/>
    <rect class="rocker-stripe" x="150" y="246" width="410" height="12" fill="var(--lime)"/>
    <text class="tagline" x="272" y="186" font-size="18" fill="var(--leaf)" text-anchor="end">KITCHEN AND BATH</text>
    <text class="tagline" x="272" y="207" font-size="18" fill="var(--leaf)" text-anchor="end">REMODELING COMPANY</text>
    <rect class="brand-frame" x="512" y="24" width="250" height="80" fill="none" stroke="var(--olive)" stroke-width="4"/>
    <text class="brand-name" x="637" y="78" font-size="32" fill="var(--paper)" text-anchor="middle">NORVALE DESIGN</text>
    <text class="service-line" x="637" y="138" font-size="24" fill="var(--paper)" text-anchor="middle">KITCHEN + BATH</text>
    <text class="phone" x="612" y="177" font-size="29" fill="var(--paper)" text-anchor="middle">+123 456 789</text>
    <text class="web" x="612" y="208" font-size="16" fill="var(--paper)" text-anchor="middle">NORVALEDESIGN.COM</text>
  </svg>

  <!-- Pickup truck wrap -->
  <svg class="wrap-panel wrap-truck" viewBox="0 0 795 270" aria-label="Pickup truck wrap layout">
    <rect class="body-base" x="0" y="20" width="795" height="230" rx="20" fill="var(--body)"/>
    <path class="black-field" d="M470 20 H775 Q795 20 795 40 V105 H470 Z" fill="var(--ink)"/>
    <rect class="olive-band" x="470" y="105" width="325" height="45" fill="var(--olive)"/>
    <rect class="leaf-band" x="470" y="150" width="325" height="70" fill="var(--leaf)"/>
    <rect class="leaf-band front" x="130" y="178" width="340" height="42" fill="var(--leaf)"/>
    <path class="rocker" d="M0 220 H795 V230 Q795 250 775 250 H20 Q0 250 0 230 Z" fill="var(--rocker)"/>
    <circle class="brand-ring" cx="400" cy="135" r="78" fill="var(--body)" stroke="var(--ring)" stroke-width="10"/>
    <text class="brand-name" x="400" y="146" font-size="30" fill="var(--leaf)" text-anchor="middle">NORVALE</text>
    <rect class="brand-frame" x="150" y="88" width="150" height="56" fill="none" stroke="var(--olive)" stroke-width="3"/>
    <text class="brand-name" x="225" y="122" font-size="17" fill="var(--leaf)" text-anchor="middle">NORVALE DESIGN</text>
    <text class="small-service" x="225" y="164" font-size="13" fill="var(--ink)" text-anchor="middle">KITCHEN + BATH</text>
    <text class="tagline" x="225" y="205" font-size="15" fill="var(--paper)" text-anchor="middle">A HERITAGE OF INNOVATION</text>
    <text class="tagline" x="635" y="72" font-size="18" fill="var(--paper)" text-anchor="middle">KITCHEN AND BATH REMODELING COMPANY</text>
    <text class="phone" x="492" y="136" font-size="22" fill="var(--paper)">+123 456 789</text>
    <text class="web" x="500" y="170" font-size="13" fill="var(--paper)">NORVALEDESIGN.COM</text>
  </svg>

  <!-- Enclosed trailer wrap -->
  <svg class="wrap-panel wrap-trailer" viewBox="0 0 795 490" aria-label="Enclosed trailer wrap layout">
    <rect class="body-base" x="0" y="0" width="795" height="480" rx="10" fill="var(--body)"/>
    <path class="black-field" d="M320 0 H785 Q795 0 795 10 V260 H320 Z" fill="var(--ink)"/>
    <rect class="olive-band" x="320" y="260" width="475" height="60" fill="var(--olive)"/>
    <rect class="leaf-band" x="320" y="320" width="475" height="62" fill="var(--leaf)"/>
    <path class="lime-band" d="M0 382 H795 V470 Q795 480 785 480 H10 Q0 480 0 470 Z" fill="var(--lime)"/>
    <circle class="brand-ring" cx="250" cy="205" r="150" fill="var(--body)" stroke="var(--ring)" stroke-width="20"/>
    <text class="brand-name" x="250" y="228" font-size="64" fill="var(--leaf)" text-anchor="middle">NORVALE</text>
    <rect class="brand-frame" x="430" y="28" width="330" height="140" fill="none" stroke="var(--olive)" stroke-width="5"/>
    <text class="brand-name" x="595" y="118" font-size="46" fill="var(--paper)" text-anchor="middle">NORVALE DESIGN</text>
    <text class="service-line" x="595" y="230" font-size="34" fill="var(--paper)" text-anchor="middle">KITCHEN + BATH</text>
    <text class="phone" x="580" y="308" font-size="46" fill="var(--paper)" text-anchor="middle">+123 456 789</text>
    <text class="web" x="580" y="366" font-size="34" fill="var(--paper)" text-anchor="middle">NORVALEDESIGN.COM</text>
    <text class="tagline" x="575" y="422" font-size="36" fill="var(--paper)" text-anchor="middle">KITCHEN AND BATH</text>
    <text class="tagline" x="575" y="464" font-size="36" fill="var(--paper)" text-anchor="middle">REMODELING COMPANY</text>
  </svg>

</main>
</body>
</html>
```